Book Cover Design Project

Design a cover for a children's book. The book is both an educational tool and a Christian devotional. The subject of the book is the biography of Harold Penbrook and contains short descriptions of events from Penbrook's life as well as Christian devotions derived from those events. See attached back-cover material for more information.

Requirements
Must have
• 1. Red, White and Blue for colors.
2. The Silver Lantern Publishing logo which is attached in B&W or color.
3. Title "The Harold Penbrook Reader: Lessons in Faith and Learning"
4. Back cover material which is attached.

```html
<!DOCTYPE html>
<html lang="en">
<head>
<meta charset="UTF-8">
<title>The Harold Penbrook Reader: Lessons in Faith and Learning</title>
<link rel="stylesheet" href="https://fonts.googleapis.com/css2?family=Rubik+Dirt&family=Special+Elite&family=Open+Sans:wght@600&display=swap">
<style>
  :root {
    --page-bg: #e8e8ec;
    --cover-white: #ffffff;
    --floor-grey: #ececec;
    --flag-blue: #2a4fa3;
    --flag-red: #b01d27;
    --panel-red: #9c1b25;
    --ink: #111111;
    --paper-text: #ffffff;
    --logo-grey: #333333;
  }
  * { box-sizing: border-box; margin: 0; padding: 0; }
  html, body {
    width: 1200px;
    height: 900px;
    overflow: hidden;
    background: var(--page-bg);
  }
  .canvas {
    position: relative;
    width: 1200px;
    height: 900px;
  }
  .cover {
    position: absolute;
    left: 320px;
    top: 30px;
    width: 560px;
    height: 840px;
    background: var(--cover-white);
    overflow: hidden;
    box-shadow: 0 6px 24px rgba(0,0,0,0.15);
  }
  .cover-shapes {
    position: absolute;
    inset: 0;
    width: 560px;
    height: 840px;
  }
  .portrait-area {
    position: absolute;
    left: 34px;
    top: 70px;
    width: 220px;
    height: 620px;
    border-radius: 40px 40px 10px 10px;
    background: linear-gradient(180deg, #e9e3da 0%, #1b1b1b 35%, #111 80%, #2a2a2a 100%);
    opacity: 0.9;
  }
  .title {
    position: absolute;
    left: 285px;
    top: 205px;
    width: 260px;
    font-family: "Rubik Dirt", "Special Elite", sans-serif;
    color: var(--ink);
    line-height: 1;
  }
  .title span { display: block; }
  .title-the { font-size: 28px; margin-left: 6px; }
  .title-first { font-size: 56px; margin-top: 12px; letter-spacing: 1px; }
  .title-last { font-size: 40px; margin-top: 10px; margin-left: 40px; }
  .title-kind { font-size: 28px; margin-top: 10px; margin-left: 80px; }
  .subtitle {
    position: absolute;
    left: 290px;
    top: 615px;
    width: 250px;
    font-family: "Rubik Dirt", "Special Elite", sans-serif;
    color: var(--paper-text);
    font-size: 33px;
    line-height: 1.2;
    text-align: center;
  }
  .publisher {
    position: absolute;
    left: 0;
    right: 0;
    top: 770px;
    display: flex;
    justify-content: center;
    align-items: center;
    gap: 14px;
    font-family: "Open Sans", sans-serif;
    font-weight: 600;
    font-size: 24px;
    color: var(--logo-grey);
  }
  .publisher-mark {
    width: 30px;
    height: 30px;
    background: var(--logo-grey);
  }
</style>
</head>
<body>
<main class="canvas">
  <section class="cover">
    <svg class="cover-shapes" viewBox="0 0 560 840" aria-hidden="true">
      <rect class="floor" x="0" y="600" width="560" height="240" fill="var(--floor-grey)"/>
      <polygon class="red-backdrop" points="0,95 232,75 262,640 0,675" fill="var(--panel-red)"/>
      <polygon class="title-box" points="268,585 560,545 560,760 268,760" fill="var(--flag-red)"/>
    </svg>
    <div class="stars-band" role="img" aria-label="Blue band with rows of white stars"
         style="position:absolute;left:0;top:0;width:560px;height:120px;background:linear-gradient(180deg,#2f57ad,#24479a);clip-path:polygon(0 0,100% 0,100% 55%,0 100%);"></div>
    <div class="portrait-area" role="img" aria-label="Cartoon illustration of Harold Penbrook standing in colonial dress with a sword"></div>
    <h1 class="title">
      <span class="title-the">The</span>
      <span class="title-first">HAROLD</span>
      <span class="title-last">Penbrook</span>
      <span class="title-kind">Reader:</span>
    </h1>
    <p class="subtitle">Lessons in<br>Faith and<br>Learning</p>
    <div class="publisher">
      <span class="publisher-mark"></span>
      <span class="publisher-name">Silver Lantern Publishing</span>
    </div>
  </section>
</main>
</body>
</html>
```